Brackwell HVAC Service LLC Business Card

We just got a design created by one of your designers for a logo and now would like help with a business card design. The information to be included on the card is as follows:
Brackwell HVAC Service LLC (I will attach logo design)
P.O. Box 418
Carlow, CO 80694
(970) 555-0147
Dale Vonnholt
I might include an e-mail address, but I'm not sure yet.
Target Market(s)
Customers needing service or repairs done on their heating and air conditioning systems.
Industry/Entity Type
Business
Contact Information for Business Card
P.O. Box 418
Carlow, CO 80694
(970) 555-0147
Dale Vonnholt

```html
<!DOCTYPE html>
<html lang="en">
<head>
<meta charset="utf-8">
<title>Brackwell HVAC Service LLC – Business Card</title>
<link href="https://fonts.googleapis.com/css2?family=Oxygen:wght@400;700&display=swap" rel="stylesheet">
<style>
  :root {
    --page-bg: #2a2a2c;
    --card-bg: #f4f4f4;
    --brand-red: #d3242b;
    --brand-blue: #1f3f7a;
    --ink: #1c1c1c;
    --rule: #1f3f7a;
  }
  * { box-sizing: border-box; margin: 0; padding: 0; }
  html, body { width: 1200px; height: 900px; overflow: hidden; }
  body {
    background: var(--page-bg);
    font-family: "Oxygen", Arial, sans-serif;
    position: relative;
  }
  .card {
    position: absolute;
    left: 300px;
    width: 600px;
    height: 343px;
    background: var(--card-bg);
    box-shadow: 0 10px 30px rgba(0,0,0,.45);
  }
  .card--front { top: 70px; }
  .card--back { top: 487px; }

  .front-brand {
    position: absolute;
    inset: 0;
    display: flex;
    align-items: center;
    justify-content: center;
    gap: 14px;
  }
  .brand-dot {
    width: 34px; height: 34px;
    border-radius: 50%;
    background: var(--brand-red);
  }
  .brand-name {
    font-weight: 700;
    color: var(--brand-blue);
    letter-spacing: .5px;
  }
  .front-brand .brand-name { font-size: 30px; }

  .back-brand {
    position: absolute;
    left: 48px; top: 64px;
    display: flex; align-items: center; gap: 10px;
  }
  .back-brand .brand-dot { width: 22px; height: 22px; }
  .back-brand .brand-name { font-size: 17px; }

  .divider {
    position: absolute;
    left: 48px; top: 150px;
    width: 290px; height: 2px;
    background: var(--rule);
  }
  .holder-name {
    position: absolute;
    left: 345px; top: 118px;
    font-size: 22px;
    color: var(--brand-blue);
  }
  .address {
    position: absolute;
    left: 60px; top: 186px;
    font-size: 15px;
    line-height: 1.45;
    color: var(--ink);
    font-style: normal;
  }
  .address .company { color: var(--brand-red); }
  .contact {
    position: absolute;
    left: 345px; top: 160px;
    font-size: 13.5px;
    line-height: 1.5;
    color: var(--ink);
    list-style: none;
  }
  .contact .label { color: var(--brand-red); margin-right: 4px; }
</style>
</head>
<body>
  <section class="card card--front" aria-label="Card front">
    <div class="front-brand">
      <span class="brand-dot"></span>
      <span class="brand-name">Brackwell HVAC Service LLC</span>
    </div>
  </section>

  <section class="card card--back" aria-label="Card back">
    <div class="back-brand">
      <span class="brand-dot"></span>
      <span class="brand-name">Brackwell HVAC Service LLC</span>
    </div>
    <div class="divider"></div>
    <p class="holder-name">Dale Vonnholt</p>
    <ul class="contact">
      <li><span class="label">P :</span>(970) 555-0147</li>
      <li><span class="label">E :</span>Dale@BrackwellHvacServices.com</li>
      <li>www.BrackwellHvacServices.com</li>
    </ul>
    <address class="address">
      <span class="company">Brackwell HVAC Service LLC</span><br>
      P.O. Box 418<br>
      Carlow, CO 80694
    </address>
  </section>
</body>
</html>
```